Marketing collateral for KESTA a ladies wellness center and spa
KESTA mind and body wellness
mind and body wellness
i need a design for marketing and adds
Salon & Spa
==============Update==============
I would like it to be a Tri-Fold brochure design.
Our center consists of different services we divide them into spa,
physiotherapy , psychology and dermatology. i know i can't jam in all
images in a one brochure design but give me your best at it, as for the
images from prime frame photo:
1) pebble trove 40926318
2) crimson lens cq5093416
3) choose any number of pictures i attached of our center.
this is the logo with black background
G with black background
this is the logo with WHITE background
G with WHITE background
Business Card Front
Business Card Back
Latterhead

```html
<!DOCTYPE html>
<html lang="en">
<head>
<meta charset="utf-8">
<title>KESTA mind and body wellness – tri-fold brochure</title>
<link href="https://fonts.googleapis.com/css2?family=Cinzel:wght@400;600&family=Lato:wght@400;700&display=swap" rel="stylesheet">
<style>
:root{
  --stage:#2b2622;
  --ink:#0d0c0b;
  --panel:#161412;
  --gold:#c9a24a;
  --gold-light:#f1d98a;
  --gold-deep:#7a5a1c;
  --text:#e9e3d6;
  --muted:#b7ab92;
}
*{box-sizing:border-box;margin:0;padding:0}
html,body{width:1200px;height:850px;overflow:hidden;background:var(--stage)}
body{font-family:"Lato",sans-serif;color:var(--text);position:relative}
.spread{position:absolute;left:45px;width:1110px;height:390px;display:flex;box-shadow:0 6px 18px rgba(0,0,0,.5)}
.spread--outside{top:20px}
.spread--inside{top:440px}
.panel{position:relative;width:370px;height:100%;background:linear-gradient(180deg,var(--panel),var(--ink));overflow:hidden;border-right:1px solid #000}
.panel:last-child{border-right:none}
.swoosh{position:absolute;left:0;width:100%}
.photo{position:absolute;border-radius:2px}
.photo--lips{left:40px;top:70px;width:120px;height:70px;background:linear-gradient(135deg,#e8cfc4,#b5656a 60%,#e8cfc4)}
.photo--stones{left:40px;top:150px;width:120px;height:70px;background:linear-gradient(135deg,#f4f4f2,#c9c9c5)}
.photo--interior{background:linear-gradient(160deg,#3a2a12,#b07c2c 45%,#4a3414 80%,#1c140a)}
.photo--gold{background:radial-gradient(circle at 60% 40%,var(--gold-light),var(--gold) 45%,var(--gold-deep))}
.hours{position:absolute;left:40px;top:120px;width:290px}
.heading{font-family:"Cinzel",serif;color:var(--gold);letter-spacing:2px;font-weight:600}
.hours .heading{font-size:22px;margin-bottom:8px}
.hours-row{display:flex;justify-content:space-between;font-size:12px;line-height:20px;color:var(--text);width:200px}
.contact{position:absolute;left:40px;top:280px;font-size:11px;line-height:17px;color:var(--muted)}
.contact strong{color:var(--gold);font-weight:700}
.brand{position:absolute;left:0;width:100%;text-align:center;top:120px}
.brand-name{display:inline-flex;align-items:center;gap:10px;font-family:"Cinzel",serif;font-size:40px;color:var(--ink);letter-spacing:4px;font-weight:600}
.brand-dot{width:16px;height:16px;border-radius:50%;background:var(--ink)}
.brand-tag{font-size:12px;letter-spacing:3px;color:var(--ink);margin-top:4px;text-transform:lowercase}
.content{position:absolute;left:28px;right:24px;top:138px}
.content .heading{font-size:14px;margin-bottom:2px}
.sub{font-size:10px;color:var(--gold-light);letter-spacing:1px;text-transform:uppercase;margin-bottom:6px}
.list{list-style:none;font-size:10.5px;line-height:15px;margin-bottom:10px}
.list li{padding-left:12px;position:relative}
.list li::before{content:"";position:absolute;left:0;top:5px;width:5px;height:5px;background:var(--gold)}
.cols{display:flex;gap:18px}
.cols>div{flex:1}
</style>
</head>
<body>

<section class="spread spread--outside" aria-label="Brochure outside">
  <article class="panel panel--flap">
    <svg class="swoosh" style="top:0" width="370" height="260" viewBox="0 0 370 260" aria-hidden="true">
      <defs><linearGradient id="g1" x1="0" y1="0" x2="1" y2="1"><stop offset="0" stop-color="#f1d98a"/><stop offset=".5" stop-color="#c9a24a"/><stop offset="1" stop-color="#7a5a1c"/></linearGradient></defs>
      <path d="M0 0H370V150C260 120 120 210 0 250Z" fill="url(#g1)"/>
      <path d="M0 258C120 218 260 128 370 158" stroke="#f1d98a" stroke-width="2" fill="none"/>
    </svg>
    <div class="photo photo--lips" role="img" aria-label="Close-up photo of lips for the dermatology service"></div>
    <div class="photo photo--stones" role="img" aria-label="Photo of white spa stones"></div>
  </article>

  <article class="panel panel--info">
    <svg class="swoosh" style="top:0" width="370" height="100" viewBox="0 0 370 100" aria-hidden="true">
      <path d="M0 0H370V30C250 80 120 40 0 90Z" fill="url(#g1)"/>
    </svg>
    <div class="hours">
      <h2 class="heading">HOURS</h2>
      <div class="hours-row"><span>Saturday</span><span>9:00 – 9:00</span></div>
      <div class="hours-row"><span>Sunday</span><span>9:00 – 9:00</span></div>
      <div class="hours-row"><span>Monday</span><span>9:00 – 9:00</span></div>
      <div class="hours-row"><span>Tuesday</span><span>9:00 – 9:00</span></div>
      <div class="hours-row"><span>Wednesday</span><span>9:00 – 9:00</span></div>
      <div class="hours-row"><span>Thursday</span><span>9:00 – 6:00</span></div>
    </div>
    <address class="contact" style="font-style:normal">
      <strong>KESTA</strong><br>
      14 Palm Crescent, Tefro<br>
      Tel +000 11 555 0142<br>
      hello@kesta-wellness.com
    </address>
  </article>

  <article class="panel panel--cover">
    <svg class="swoosh" style="top:0" width="370" height="390" viewBox="0 0 370 390" aria-hidden="true">
      <path d="M0 0H370V220C250 200 120 260 0 230Z" fill="url(#g1)"/>
      <path d="M0 240C120 270 250 210 370 230" stroke="#f1d98a" stroke-width="2" fill="none"/>
    </svg>
    <div class="brand">
      <div class="brand-name"><span class="brand-dot"></span>KESTA</div>
      <div class="brand-tag">mind and body wellness</div>
    </div>
    <div class="photo photo--interior" style="left:0;top:250px;width:370px;height:140px" role="img" aria-label="Photo of the spa interior with warm lighting"></div>
  </article>
</section>

<section class="spread spread--inside" aria-label="Brochure inside">
  <article class="panel">
    <div class="photo photo--interior" style="left:0;top:0;width:370px;height:120px" role="img" aria-label="Photo of the physiotherapy room"></div>
    <svg class="swoosh" style="top:70px" width="370" height="60" viewBox="0 0 370 60" aria-hidden="true">
      <path d="M0 60V40C120 0 250 30 370 10V60Z" fill="#161412"/>
      <path d="M0 40C120 0 250 30 370 10" stroke="#c9a24a" stroke-width="3" fill="none"/>
    </svg>
    <div class="content">
      <h3 class="heading">PHYSIOTHERAPY CLINIC</h3>
      <p class="sub">Choose a stretching treatment</p>
      <ul class="list">
        <li>Deep circulation therapy</li><li>Core strengthening</li><li>Back pain relief</li><li>Guided stretching</li>
      </ul>
      <p class="sub">Body treatments</p>
      <ul class="list">
        <li>Posture training</li><li>Joint mobility care</li><li>Sports recovery</li><li>Neck and shoulder care</li><li>Balance and movement work</li><li>Relaxing massage</li>
      </ul>
    </div>
  </article>

  <article class="panel">
    <div class="photo photo--gold" style="left:0;top:0;width:370px;height:120px" role="img" aria-label="Photo of a skin care treatment"></div>
    <svg class="swoosh" style="top:70px" width="370" height="60" viewBox="0 0 370 60" aria-hidden="true">
      <path d="M0 60V20C120 50 250 0 370 30V60Z" fill="#161412"/>
      <path d="M0 20C120 50 250 0 370 30" stroke="#f1d98a" stroke-width="3" fill="none"/>
    </svg>
    <div class="content">
      <h3 class="heading">DERMATOLOGY CLINIC</h3>
      <p class="sub">Skin plans made for every woman</p>
      <div class="cols">
        <ul class="list"><li>Acne care</li><li>Skin peels</li><li>Laser hair removal</li><li>Pigment care</li><li>Facial renewal</li></ul>
        <ul class="list"><li>Scar treatment</li><li>Hydration therapy</li><li>Anti-aging care</li><li>Nail care</li><li>Skin analysis</li></ul>
      </div>
    </div>
  </article>

  <article class="panel">
    <div class="photo photo--interior" style="left:0;top:0;width:370px;height:120px" role="img" aria-label="Photo of the spa lounge"></div>
    <svg class="swoosh" style="top:70px" width="370" height="60" viewBox="0 0 370 60" aria-hidden="true">
      <path d="M0 60V30C120 0 250 40 370 15V60Z" fill="#161412"/>
      <path d="M0 30C120 0 250 40 370 15" stroke="#c9a24a" stroke-width="3" fill="none"/>
    </svg>
    <div class="content">
      <h3 class="heading">SPA</h3>
      <ul class="list">
        <li>Moroccan bath</li><li>Aromatherapy massage</li><li>Hot stone therapy</li><li>Body scrub and wrap</li>
      </ul>
      <h3 class="heading">PSYCHOLOGY CLINIC</h3>
      <ul class="list">
        <li>Anxiety support</li><li>Stress management</li><li>Family counseling</li><li>Sleep guidance</li><li>Confidence coaching</li>
      </ul>
    </div>
  </article>
</section>

</body>
</html>
```